Fresh Tarrow Work Post - Business Card Required

Dear All,

I own Velmira Limited, which in turn owns the website:
www.harbinworkpost.example

I want all of you wonderful creative people to come up with a slick, and awesome business card design that incorporates the logo on the site, and some colouring and design elements from it.

You have free reign in how you go about doing this, I won't be giving my contact details on this platform, but the winner will be asked to redesign based on my contact details which I will supply at the end.

I need the design to be completed within 5 days. I need the final print copies of the business cards by the 25th November, so unfortunately it's a bit of a rush to get these designs ready.

Any questions, please ask.

Thank you
Updates

Thank you all for your hard work and exceptional designs provided. I do have to pick one, so I have a very clear idea of which one this is, however I will wait one further day until the competition closes to be fair to all those have submitted, or are in the process of submitting. I wish you all the best and thank you again for your dedication.

```html
<!DOCTYPE html>
<html lang="en">
<head>
<meta charset="utf-8">
<title>Harbin Work Post – Business Card</title>
<link rel="stylesheet" href="https://fonts.googleapis.com/css2?family=Questrial&display=swap">
<style>
  :root {
    --stage: #ececee;
    --card: #272727;
    --gold: #c9a24a;
    --gold-dark: #94702c;
    --gold-light: #e0cb7a;
    --ink-light: #f4f4f4;
  }
  html, body {
    margin: 0;
    padding: 0;
    overflow: hidden;
  }
  body {
    width: 1200px;
    height: 600px;
    background: var(--stage);
    position: relative;
    font-family: "Questrial", sans-serif;
  }
  .card {
    position: absolute;
    top: 161px;
    width: 467px;
    height: 278px;
    background: var(--card);
    overflow: hidden;
    box-shadow: 0 6px 14px rgba(0,0,0,0.18);
  }
  .card--front { left: 93px; }
  .card--back { left: 638px; }
  .card__band {
    position: absolute;
    left: 0; top: 0;
    width: 100%;
    height: 16px;
    background: linear-gradient(90deg, var(--gold-dark), var(--gold-light) 55%, var(--gold-dark));
  }
  .card__lines {
    position: absolute;
    left: 0; top: 0;
  }
  .brand-mark {
    position: absolute;
    border: 2px solid var(--gold);
    border-radius: 50%;
  }
  .card--front .brand-mark {
    left: 191px; top: 54px;
    width: 80px; height: 80px;
  }
  .brand-name {
    position: absolute;
    color: var(--gold);
    white-space: nowrap;
    text-transform: uppercase;
  }
  .card--front .brand-name {
    left: 111px; top: 203px;
    width: 244px;
    text-align: center;
    font-size: 19px;
    letter-spacing: 2px;
  }
  .card--back .brand-mark {
    left: 150px; top: 42px;
    width: 52px; height: 52px;
  }
  .card--back .brand-name {
    left: 96px; top: 103px;
    width: 160px;
    text-align: center;
    font-size: 10px;
    letter-spacing: 1px;
  }
  .person {
    position: absolute;
    left: 266px; top: 54px;
    color: var(--ink-light);
  }
  .person__name {
    margin: 0;
    font-size: 24px;
    font-weight: 400;
    letter-spacing: 0.5px;
    line-height: 1;
  }
  .person__role {
    margin: 2px 0 0;
    font-size: 11px;
  }
  .website {
    position: absolute;
    left: 26px; top: 216px;
    font-size: 11px;
    color: var(--ink-light);
  }
  .contact {
    position: absolute;
    left: 234px; top: 187px;
    font-size: 11px;
    line-height: 15px;
    color: var(--ink-light);
  }
  .contact__tagline {
    color: var(--gold);
    text-transform: uppercase;
    margin-bottom: 1px;
  }
  .contact__row {
    display: flex;
    align-items: center;
    gap: 5px;
  }
  .contact__icon { flex: none; }
</style>
</head>
<body>

  <section class="card card--front" aria-label="Card front">
    <div class="card__band"></div>
    <div class="brand-mark"></div>
    <svg class="card__lines" width="467" height="278" aria-hidden="true">
      <line x1="111" y1="198" x2="355" y2="198" stroke="#c9a24a" stroke-width="1.5"/>
      <line x1="111" y1="229" x2="355" y2="229" stroke="#c9a24a" stroke-width="1.5"/>
    </svg>
    <div class="brand-name">Harbin Work Post</div>
  </section>

  <section class="card card--back" aria-label="Card back">
    <div class="card__band"></div>
    <svg class="card__lines" width="467" height="278" aria-hidden="true">
      <line x1="106" y1="16" x2="0" y2="264" stroke="#c9a24a" stroke-width="1"/>
      <line x1="266" y1="16" x2="162" y2="278" stroke="#c9a24a" stroke-width="1"/>
      <line x1="0" y1="126" x2="467" y2="126" stroke="#c9a24a" stroke-width="2.5"/>
      <line x1="0" y1="202" x2="467" y2="202" stroke="#c9a24a" stroke-width="0.8"/>
      <line x1="0" y1="248" x2="467" y2="248" stroke="#c9a24a" stroke-width="0.8"/>
    </svg>
    <div class="brand-mark"></div>
    <div class="brand-name">Harbin Work Post</div>

    <div class="person">
      <h1 class="person__name">CORWEN TALBY</h1>
      <p class="person__role">Managing Director</p>
    </div>

    <div class="website">www.harbinworkpost.example</div>

    <div class="contact">
      <div class="contact__tagline">Search for your next job</div>
      <div class="contact__row">17 Quillan Row, Tarrow, TW4 9QX</div>
      <div class="contact__row">
        <svg class="contact__icon" width="9" height="11" viewBox="0 0 9 11" aria-label="Phone">
          <rect x="1.5" y="0.5" width="6" height="10" rx="1" fill="none" stroke="#c9a24a"/>
          <rect x="3" y="2" width="3" height="3" fill="#c9a24a"/>
        </svg>
        0700 555 0142
      </div>
      <div class="contact__row">
        <svg class="contact__icon" width="12" height="9" viewBox="0 0 12 9" aria-label="Email">
          <rect x="0.5" y="0.5" width="11" height="8" fill="none" stroke="#c9a24a"/>
          <polyline points="0.5,0.5 6,5 11.5,0.5" fill="none" stroke="#c9a24a"/>
        </svg>
        contact@harbinworkpost.example
      </div>
    </div>
  </section>

</body>
</html>
```